Makeup Artist Requires Business Card design

Hi

I am looking for a business card design to market my makeup artist business. I operate under my own name Hazel Drummet and I would like to keep the design of the card very simplistic and chic - something that keeps both my name and profession (makeup artist) the focus of the card. I would like it to be a style that is eyecatching to the reader (i am open to anything unusual) but upmarket.

Target Market(s)

women, magazine/beauty/fashion editors, photographers.

Industry/Entity Type

Business

Requirements
Must have
• Must contain:

Phone number: 0417 382 915
Website: www.hazeldrummet.com.au
email: contact@hazeldrummet.com.au

(although you don't need to have prefaced these with the words phone number, website etc :))
Should not have
• I am not looking for anything overly colorful - my preference is to keep the card dark if possible.

```html
<!DOCTYPE html>
<html lang="en">
<head>
<meta charset="utf-8">
<title>Hazel Drummet – Makeup Artist Business Card</title>
<link rel="stylesheet" href="https://fonts.googleapis.com/css2?family=Josefin+Sans:wght@300;400&family=Arimo:wght@400&display=swap">
<style>
  :root {
    --backdrop: #ececec;
    --card-grey: #68686a;
    --panel-deep: #050505;
    --panel-lift: #3c3c3e;
    --brand-blue: #4fc3ea;
    --ink-light: #e6e6e6;
    --ink-dark: #1b1b1b;
    --icon-disc: #c4c4c4;
    --icon-ink: #3a3a3a;
  }
  html, body {
    margin: 0;
    width: 1200px;
    height: 959px;
    overflow: hidden;
    background: var(--backdrop);
  }
  .stage { display: block; width: 1200px; height: 959px; }
  .card { filter: drop-shadow(4px 6px 6px rgba(0,0,0,0.45)); }
  .card-base { fill: var(--card-grey); }
  .brand-name {
    font-family: "Josefin Sans", sans-serif;
    font-weight: 300;
    fill: var(--brand-blue);
  }
  .profession {
    font-family: "Josefin Sans", sans-serif;
    font-weight: 400;
    letter-spacing: 2.6px;
  }
  .profession--light { fill: var(--ink-light); }
  .profession--dark { fill: var(--ink-dark); }
  .contact-text {
    font-family: "Arimo", sans-serif;
    font-size: 12px;
    fill: #ffffff;
  }
  .icon-disc { fill: var(--icon-disc); }
  .icon-ink { fill: none; stroke: var(--icon-ink); stroke-width: 1.3; }
  .icon-fill { fill: var(--icon-ink); }
</style>
</head>
<body>
<svg class="stage" viewBox="0 0 1200 959" xmlns="http://www.w3.org/2000/svg">
  <defs>
    <radialGradient id="panel-glow" cx="0.5" cy="0.38" r="0.62">
      <stop offset="0" stop-color="var(--panel-lift)"/>
      <stop offset="1" stop-color="var(--panel-deep)"/>
    </radialGradient>
  </defs>

  <!-- Front of card -->
  <g class="card card--front" transform="translate(207 130) scale(1.1516)">
    <path class="card-base" d="M0,120 Q0,0 120,0 H300 V519 H0 Z"/>
    <path fill="url(#panel-glow)" d="M0,120 Q0,0 120,0 H160 C245,0 298,60 298,150 V488 C170,488 40,420 0,280 Z"/>

    <text class="brand-name" x="24" y="62" font-size="33">Hazel</text>
    <text class="brand-name" x="24" y="104" font-size="33">Drummet</text>
    <text class="profession profession--light" x="25" y="182" font-size="10.5">MAKEUP ARTIST</text>

    <!-- phone -->
    <g class="contact contact--phone">
      <circle class="icon-disc" cx="49" cy="323" r="14"/>
      <rect class="icon-ink" x="44" y="314" width="10" height="18" rx="1.5"/>
      <rect class="icon-fill" x="46" y="317" width="6" height="7"/>
      <text class="contact-text" x="69" y="327">0417 382 915</text>
    </g>
    <!-- email -->
    <g class="contact contact--email">
      <circle class="icon-disc" cx="79" cy="365" r="14"/>
      <path class="icon-ink" d="M71,362 L79,356 L87,362 V372 H71 Z M71,362 L79,368 L87,362"/>
      <text class="contact-text" x="101" y="369">contact@hazeldrummet.com.au</text>
    </g>
    <!-- web -->
    <g class="contact contact--web">
      <circle class="icon-disc" cx="118" cy="408" r="14"/>
      <circle class="icon-ink" cx="118" cy="408" r="8"/>
      <ellipse class="icon-ink" cx="118" cy="408" rx="3.5" ry="8"/>
      <path class="icon-ink" d="M110,408 H126 M111.5,404 H124.5 M111.5,412 H124.5"/>
      <text class="contact-text" x="140" y="412">www.hazeldrummet.com.au</text>
    </g>
  </g>

  <!-- Back of card -->
  <g class="card card--back" transform="translate(671 284) scale(1.1516)">
    <path class="card-base" d="M0,90 Q0,0 95,0 H299 V519 H0 Z"/>
    <text class="brand-name" x="150" y="200" font-size="50" text-anchor="middle">Hazel</text>
    <text class="brand-name" x="150" y="262" font-size="50" text-anchor="middle">Drummet</text>
    <text class="profession profession--dark" x="151" y="373" font-size="14.5" text-anchor="middle" style="letter-spacing:3.4px">MAKEUP ARTIST</text>
  </g>
</svg>
</body>
</html>
```